Insurance company needs a business card design

We need a business card design for a Massachusetts-based insurance company Veloria Insurance, LLC. We provide auto insurance to Hispanic (Spanish- or Portuguese-speaking) immigrants in the United States. We will give these business cards to auto dealers where such customers typically go to purchase vehicles. We will provide a solution to the dealers to provide easy insurance to the customers buying cars at their dealerships. Veloria is the Spanish word for protection.
Contact Information for Business Card
Name, Designation, Company Name, Address, Phone Number, Email, Website
Look and feel
Each slider illustrates characteristics of the customer's brand and the style your logo design should communicate.

```html
<!DOCTYPE html>
<html lang="en">
<head>
<meta charset="utf-8">
<title>Veloria Insurance – Business Card</title>
<link href="https://fonts.googleapis.com/css2?family=Montserrat:wght@500;700;800&family=Arimo:wght@400&display=swap" rel="stylesheet">
<style>
  :root {
    --navy: #0b4a80;
    --orange: #ef8507;
    --white: #ffffff;
    --backdrop: #3a3a3a;
  }
  html, body {
    margin: 0;
    padding: 0;
    width: 1200px;
    height: 1015px;
    overflow: hidden;
    background: var(--backdrop);
  }
  .stage {
    width: 1200px;
    height: 1015px;
    display: flex;
    flex-direction: column;
    align-items: center;
    justify-content: center;
    gap: 56px;
  }
  .card {
    width: 700px;
    height: 400px;
    position: relative;
    box-shadow: 0 12px 30px rgba(0,0,0,.55);
    overflow: hidden;
  }
  .card-front {
    background: var(--white);
    display: flex;
    align-items: center;
    justify-content: center;
  }
  .brand {
    display: flex;
    align-items: center;
    gap: 18px;
  }
  .brand-mark {
    width: 56px;
    height: 56px;
    background: var(--orange);
  }
  .brand-name {
    font-family: "Montserrat", sans-serif;
    font-weight: 800;
    font-size: 46px;
    letter-spacing: 2px;
    color: var(--navy);
    line-height: 1;
  }
  .card-back {
    background: var(--navy);
    color: var(--white);
  }
  .accent-block {
    position: absolute;
    left: 44px;
    top: 150px;
    width: 28px;
    height: 46px;
    background: var(--orange);
  }
  .person {
    position: absolute;
    left: 90px;
    top: 146px;
  }
  .person-name {
    font-family: "Montserrat", sans-serif;
    font-weight: 700;
    font-size: 24px;
    color: var(--orange);
    margin: 0;
    letter-spacing: .5px;
  }
  .person-title {
    font-family: "Montserrat", sans-serif;
    font-weight: 500;
    font-size: 14px;
    margin: 4px 0 0;
    letter-spacing: .5px;
  }
  .contact-list {
    position: absolute;
    left: 90px;
    top: 228px;
    margin: 0;
    padding: 0;
    list-style: none;
    font-family: "Arimo", sans-serif;
    font-size: 16px;
  }
  .contact-list li {
    display: flex;
    align-items: center;
    gap: 10px;
    height: 24px;
  }
  .contact-list svg { width: 16px; height: 16px; }
  .address {
    position: absolute;
    left: 116px;
    top: 322px;
    margin: 0;
    font-family: "Arimo", sans-serif;
    font-size: 16px;
    line-height: 22px;
    font-style: normal;
  }
  .back-brand {
    position: absolute;
    right: 50px;
    top: 70px;
    display: flex;
    align-items: center;
    gap: 14px;
  }
  .back-brand .brand-name {
    color: var(--white);
    font-size: 40px;
  }
</style>
</head>
<body>
<main class="stage">
  <section class="card card-front" aria-label="Card front">
    <div class="brand">
      <div class="brand-mark"></div>
      <span class="brand-name">VELORIA INSURANCE</span>
    </div>
  </section>

  <section class="card card-back" aria-label="Card back">
    <div class="back-brand">
      <span class="brand-name">VELORIA</span>
    </div>

    <div class="accent-block"></div>
    <div class="person">
      <h1 class="person-name">DANIEL MORENO</h1>
      <p class="person-title">MANAGING DIRECTOR</p>
    </div>

    <ul class="contact-list">
      <li>
        <svg viewBox="0 0 16 16" aria-hidden="true"><path fill="var(--orange)" d="M3.5 1.5l2.5 3-1.5 1.6c.8 1.9 2.3 3.4 4.2 4.2l1.6-1.5 3 2.5-1.4 2.2C6.8 13.3 2.7 9.2 1.5 3z"/></svg>
        044-555 218 730
      </li>
      <li>
        <svg viewBox="0 0 16 16" aria-hidden="true"><rect x="1" y="3" width="14" height="10" fill="var(--orange)"/><path d="M1 3l7 6 7-6" fill="none" stroke="var(--navy)" stroke-width="1.4"/></svg>
        info@veloriains.com
      </li>
      <li>
        <svg viewBox="0 0 16 16" aria-hidden="true"><g fill="none" stroke="var(--orange)" stroke-width="1.4"><circle cx="8" cy="8" r="6.5"/><ellipse cx="8" cy="8" rx="3" ry="6.5"/><path d="M1.5 8h13"/></g></svg>
        www.veloriains.com
      </li>
    </ul>

    <address class="address">
      87 Harbor Street, Suite 4<br>
      Lowell, MA 01852
    </address>
  </section>
</main>
</body>
</html>
```